Etiketten für Nahrungsergänzung für Tiere
Zielgruppe
Wir stellen kolloidale Mischungen für Tiere her. Dies sind grob gesagt Nahrungsmittelergänzungen. Die Zielgruppe sind Tierbesitzer bzw. gesundheitsbewusste Menschen.
Aufgabenstellung
natürlich, in braun, beige, gold oder hellblau Tönen. Das Etikett wird auf eine Flasche aufgebraucht in der sich eine Flüssigkeit befindet. Das Etikett ist breiter als hoch. 115 x 61 mm (B x H)
Bisher haben wir blaue Flaschen verwendet und waren dadurch mit der Farbgebung ehr kühl und reduziert. In Zukunft wollen wir braune Flaschen mit schwarzen Deckel verwendet. Damit darf die Farbgebung auch wärmer, natürlich und das Etikett auch mit mehr Details versehen werden.
In den Uploads füge ich das aktuell Logo hinzu. Dies verwenden wir in braun/gold und in grün. Falls sich diese Gestaltung nicht so günstig auswirkt, haben wir ein 'alternative' Logo hinzugefügt. Da die Seite nächstes Jahr komplett überarbeitet wird und unsere Firma sich vergrößert, kann diese Änderung durchgeführt werden.
Ich lade noch ein Etikett hoch, welches wir für die Einzelelemente nutzen. Hier sind und bleiben die Flaschen nach wir vor blau (Herstellervorgaben), dadurch sind die Etikett sehr kühl und reduziert. Das darf auf den Entwurf für die Mischungen sehr gern deutlich verändert werden :-)

```html
<!DOCTYPE html>
<html lang="de">
<head>
<meta charset="utf-8">
<title>Silizium Etikett</title>
<link rel="stylesheet" href="https://fonts.googleapis.com/css2?family=Montserrat:wght@400;500;700;800&family=Oswald:wght@400;500;600&display=swap">
<style>
  :root {
    --gold: #b9953f;
    --gold-light: #cfae5e;
    --ink: #1c1a17;
    --paper: #ffffff;
    --stage: #e0d9cd;
    --cream: #f3ecdd;
  }
  * { box-sizing: border-box; margin: 0; padding: 0; }
  html, body { width: 787px; height: 1200px; overflow: hidden; background: var(--stage); }
  .label {
    position: absolute; left: 23px; top: 404px;
    width: 740px; height: 392px;
    background: var(--paper); overflow: hidden;
    font-family: "Montserrat", sans-serif; color: var(--ink);
    box-shadow: 0 4px 14px rgba(80,60,20,.12);
  }
  .label__backdrop {
    position: absolute; inset: 0;
    background:
      radial-gradient(ellipse 75% 90% at 55% 95%, rgba(255,255,255,0) 55%, rgba(243,236,221,.55) 75%, rgba(255,255,255,0) 95%),
      var(--paper);
  }
  .band-top {
    position: absolute; left: 0; top: 0; width: 100%; height: 35px;
    background: var(--gold);
    display: flex; justify-content: space-around; align-items: center;
    padding: 0 6px;
  }
  .band-top span { color: #fff; font-weight: 700; font-size: 20px; letter-spacing: 1.5px; }
  .band-bottom {
    position: absolute; left: 0; bottom: 0; width: 100%; height: 15px;
    background: var(--gold);
  }
  .batch-tab { position: absolute; left: 0; top: 0; }
  .batch-label {
    position: absolute; left: 456px; top: 352px;
    color: #fff; font-weight: 700; font-size: 13px;
  }
  .volumes {
    position: absolute; left: 208px; top: 352px;
    font-weight: 700; font-size: 13.5px;
  }
  .product-name {
    position: absolute; left: 206px; top: 342px;
    transform-origin: 0 0; transform: rotate(-90deg);
    font-weight: 800; font-size: 66px; line-height: 56px;
    color: var(--gold); letter-spacing: -1px; white-space: nowrap;
  }
  .brand {
    position: absolute; left: 279px; top: 150px; width: 182px;
    display: flex; flex-direction: column; align-items: center; gap: 10px;
  }
  .brand__dot { width: 26px; height: 26px; border-radius: 50%; background: var(--gold); }
  .brand__name { font-weight: 700; font-size: 26px; color: var(--gold); letter-spacing: 1px; }
  .facts {
    position: absolute; left: 462px; top: 132px; width: 166px;
    text-align: center;
  }
  .facts__kicker {
    font-family: "Oswald", sans-serif; font-weight: 400; font-size: 10.5px;
    line-height: 12px; text-transform: uppercase;
  }
  .facts__purity {
    font-family: "Oswald", sans-serif; font-weight: 500; font-size: 38px;
    line-height: 42px; color: var(--gold); margin-top: 2px;
  }
  .facts__claim {
    font-family: "Oswald", sans-serif; font-weight: 500; font-size: 14px;
    line-height: 15px; color: var(--gold); text-transform: uppercase;
  }
  .facts__body { font-size: 9.3px; line-height: 12px; margin-top: 12px; }
  .notes {
    position: absolute; left: 646px; top: 330px;
    width: 270px; height: 80px;
    transform-origin: 0 0; transform: rotate(-90deg);
    display: flex; flex-direction: column; justify-content: center; gap: 10px;
    text-align: center;
  }
  .notes__text { font-size: 6.6px; line-height: 9px; }
  .notes__address { font-size: 6.4px; line-height: 8px; font-weight: 700; color: var(--gold); white-space: nowrap; }
</style>
</head>
<body>
  <div class="label">
    <div class="label__backdrop" role="img" aria-label="Dezentes Hintergrundmuster aus feinen beigen Bögen"></div>

    <div class="band-top">
      <span>IONIC</span><span>IONIC</span><span>IONIC</span><span>IONIC</span>
      <span>IONIC</span><span>IONIC</span><span>IONIC</span><span>IONIC</span>
    </div>

    <div class="product-name">SILIZIUM</div>

    <div class="brand">
      <div class="brand__dot"></div>
      <div class="brand__name">Velmora</div>
    </div>

    <div class="facts">
      <p class="facts__kicker">Kolloid in wässriger<br>Lösunginhaltsstoffe:</p>
      <p class="facts__purity">99,999%</p>
      <p class="facts__claim">Reines Silizium in<br>Bidestillat</p>
      <p class="facts__body">Kolloid aus<br>Protonenresonanz verfahren55<br>ppm bei Herstellung in<br>doppelt destilliertem Wasser</p>
    </div>

    <div class="notes">
      <p class="notes__text">Bei Raumtemperatur und lichtgeschützt lagern. Vor Mikrowellen und magnetischen Feldern fernhalten. PPM-Messmethode: Atomspektralanalyse. Anwendung nach dem Quantenprinzip der verschränkten Teilchen. Nicht für den menschlichen Verzehr</p>
      <p class="notes__address">Mara Holten, Am Lindenweg 8, 07745 Talbrück</p>
    </div>

    <svg class="batch-tab" width="740" height="392" viewBox="0 0 740 392">
      <defs>
        <linearGradient id="tabGold" x1="0" x2="1" y1="0" y2="0">
          <stop offset="0" stop-color="#b9953f"/>
          <stop offset="1" stop-color="#cfae5e"/>
        </linearGradient>
      </defs>
      <path d="M412 378 C 428 378, 428 342, 450 342 L 668 342 C 684 342, 690 360, 706 378 Z" fill="url(#tabGold)"/>
    </svg>

    <div class="band-bottom"></div>

    <p class="volumes">30 ml/50 ml / 100 ml / 200 ml</p>
    <p class="batch-label">MHD-Chargen-Nr:</p>
  </div>
</body>
</html>
```